Boutique Fitness Facility needs a new meal plan design that is as hot as our workouts!

We are about to host our 6 week Coral Tide program and we need to have a great looking meal plan handout created that we can give to all of our participants.

I have attached an example of our current full meal plan, for a reference only.

As in the example I've provided, I'd like to have certain areas color coded such as the proteins being Blue, Fats -yellow, Carbs - orange and veggies- green.

These colors will corollate to the Breakfast - snack - lunch - snack - Dinner graph that I've provided and would like to have added to the new handout.

I would like our logo placed at the top and beneath the logo have the text "Coral Tide Challenge"

The flyer should be of a summer influence in colors and design and
All text should be easy to read.

Thank you and I look forward to seeing your design!

```html
<!DOCTYPE html>
<html lang="en">
<head>
<meta charset="utf-8">
<title>Coral Tide Challenge – Meal Plan</title>
<link rel="stylesheet" href="https://fonts.googleapis.com/css2?family=Barlow+Condensed:ital,wght@0,800;1,800&family=Roboto:wght@400;500;700&family=Montserrat:wght@600;700&display=swap">
<style>
  :root{
    --page-bg:#6b727a;
    --black:#0b0b0b;
    --panel-dark:#1c1c1c;
    --panel-mid:#3a3a3a;
    --yellow:#f5d20c;
    --white:#ffffff;
    --text:#3b3b3b;
    --protein-a:#1a7fd0; --protein-b:#41c2ef;
    --fats-a:#f7a21b; --fats-b:#f8d41a;
    --carbs-a:#d9431c; --carbs-b:#f47a22;
    --veg-a:#179447; --veg-b:#7cc242;
    --photo-a:#2a2a2a; --photo-b:#8a8a8a;
  }
  *{margin:0;padding:0;box-sizing:border-box}
  html,body{width:1200px;height:1200px;overflow:hidden;background:var(--page-bg)}
  .flyer{position:absolute;left:190px;top:25px;width:820px;height:1150px;background:var(--white);overflow:hidden;font-family:'Roboto',sans-serif;color:var(--text)}
  .abs{position:absolute}
  .header-art{position:absolute;left:0;top:0}
  .brand{position:absolute;left:50px;top:30px;width:265px;text-align:center}
  .brand-name{font-family:'Barlow Condensed',sans-serif;font-weight:800;font-size:78px;line-height:1;color:var(--yellow);letter-spacing:1px}
  .brand-tag{margin-top:4px;font-family:'Montserrat',sans-serif;font-weight:700;font-size:9px;letter-spacing:2.2px;color:var(--yellow)}
  .brand-tag::before,.brand-tag::after{content:"";display:inline-block;width:8px;height:9px;border-left:2px solid var(--yellow);border-right:2px solid var(--yellow);margin:0 6px;vertical-align:-1px}
  .title{position:absolute;left:58px;top:160px;font-family:'Barlow Condensed',sans-serif;font-style:italic;font-weight:800;font-size:74px;line-height:68px;color:var(--white);text-transform:uppercase;letter-spacing:1px}
  .title .accent{color:var(--yellow)}
  .card{position:absolute;top:437px;background:var(--white);border-radius:12px;box-shadow:0 2px 8px rgba(0,0,0,.18)}
  .tab{position:absolute;left:-8px;top:10px;height:30px;border-radius:4px 8px 8px 4px;font-family:'Barlow Condensed',sans-serif;font-style:italic;font-weight:800;font-size:26px;line-height:30px;color:var(--white);padding-left:20px;text-transform:uppercase}
  .tab-protein{background:linear-gradient(90deg,var(--protein-a),var(--protein-b))}
  .tab-fats{background:linear-gradient(90deg,var(--fats-a),var(--fats-b))}
  .tab-carbs{background:linear-gradient(90deg,var(--carbs-a),var(--carbs-b))}
  .tab-veg{background:linear-gradient(90deg,var(--veg-a),var(--veg-b))}
  .food-list{list-style:none;position:absolute;top:48px;left:14px;right:4px}
  .food-list li{position:relative;padding-left:17px;font-size:13.3px;line-height:16px;margin-bottom:7px;color:var(--text)}
  .food-list li::before{content:"";position:absolute;left:0;top:3px;width:9px;height:10px;background:var(--black);clip-path:polygon(0 0,45% 0,100% 50%,45% 100%,0 100%,55% 50%)}
  .food-list.protein li::before{background:linear-gradient(90deg,var(--black) 50%,var(--protein-b) 50%)}
  .food-list.fats li::before{background:linear-gradient(90deg,var(--black) 50%,var(--fats-a) 50%)}
  .food-list.carbs li::before{background:linear-gradient(90deg,var(--black) 50%,var(--carbs-a) 50%)}
  .food-list.veg li::before{background:linear-gradient(90deg,var(--black) 50%,var(--veg-b) 50%)}
  .fuel-band{position:absolute;left:0;top:786px;width:463px;height:43px;background:var(--yellow);clip-path:polygon(0 0,100% 0,93% 100%,0 100%)}
  .fuel-band span{position:absolute;left:46px;top:2px;font-family:'Barlow Condensed',sans-serif;font-style:italic;font-weight:800;font-size:32px;line-height:40px;color:var(--black);text-transform:uppercase;letter-spacing:.5px}
  .tips{position:absolute;left:0;top:829px;width:820px;height:298px}
  .tip{position:absolute;width:330px}
  .tip h3{font-family:'Barlow Condensed',sans-serif;font-style:italic;font-weight:800;font-size:23px;line-height:26px;color:var(--yellow);text-transform:uppercase;position:relative}
  .tip h3::before{content:"";position:absolute;left:-27px;top:7px;width:12px;height:13px;background:linear-gradient(90deg,var(--white) 50%,var(--yellow) 50%);clip-path:polygon(0 0,45% 0,100% 50%,45% 100%,0 100%,55% 50%)}
  .tip p{margin-top:4px;font-size:12.6px;line-height:16px;color:var(--white)}
  .visit{position:absolute;left:456px;top:1045px;width:364px;height:41px;background:var(--yellow);clip-path:polygon(0 0,100% 0,100% 100%,11% 100%)}
  .visit span{position:absolute;left:52px;top:0;font-family:'Montserrat',sans-serif;font-weight:700;font-size:21px;line-height:41px;color:var(--black)}
  .url{position:absolute;left:478px;top:1095px;font-family:'Montserrat',sans-serif;font-weight:600;font-size:19px;letter-spacing:4.5px;color:var(--black)}
</style>
</head>
<body>
<main class="flyer">
  <svg class="header-art" width="820" height="1150" viewBox="0 0 820 1150" aria-hidden="true">
    <defs>
      <linearGradient id="panelGrad" x1="0" y1="0" x2="1" y2="1">
        <stop offset="0" stop-color="#444"/><stop offset="0.6" stop-color="#1a1a1a"/><stop offset="1" stop-color="#0d0d0d"/>
      </linearGradient>
      <linearGradient id="photoGrad" x1="0" y1="0" x2="1" y2="1">
        <stop offset="0" stop-color="#9a9a9a"/><stop offset="0.5" stop-color="#5a5a5a"/><stop offset="1" stop-color="#262626"/>
      </linearGradient>
      <linearGradient id="photo2Grad" x1="0" y1="0" x2="1" y2="1">
        <stop offset="0" stop-color="#2f6fb3"/><stop offset="0.5" stop-color="#4a88c8"/><stop offset="1" stop-color="#7a4a4a"/>
      </linearGradient>
      <linearGradient id="tipsGrad" x1="0" y1="0" x2="1" y2="1">
        <stop offset="0" stop-color="#232323"/><stop offset="1" stop-color="#0a0a0a"/>
      </linearGradient>
    </defs>
    <!-- header -->
    <rect x="0" y="0" width="820" height="131" fill="var(--black)"/>
    <polygon points="0,131 460,131 350,0 0,0" fill="var(--black)"/>
    <polygon points="0,126 330,126 435,326 365,416 0,416" fill="var(--black)"/>
    <polygon points="0,139 325,139 420,326 358,410 0,410" fill="url(#panelGrad)"/>
    <polygon points="0,335 0,370 20,370" fill="var(--white)"/>
    <polyline points="0,335 55,385 310,385 320,398" fill="none" stroke="var(--yellow)" stroke-width="1.5"/>
    <g fill="var(--yellow)">
      <polygon points="325,402 340,402 360,370 345,370"/>
      <polygon points="345,402 358,402 378,370 365,370"/>
    </g>
    <g fill="var(--black)">
      <rect x="185" y="390" width="125" height="10"/>
    </g>
    <!-- main photo frame -->
    <polygon points="440,0 456,0 345,131 434,326 395,394 380,394 418,326 330,131" fill="var(--white)"/>
    <polygon points="456,0 820,0 820,286 722,394 395,394 434,326 348,131" fill="var(--white)"/>
    <polygon points="466,8 820,8 820,280 718,386 405,386 442,326 358,131" role="img" aria-label="Black and white group photo of gym members posing together on the training floor" fill="url(#photoGrad)"/>
    <g fill="var(--black)">
      <polygon points="820,300 820,322 735,402 713,402"/>
      <polygon points="820,335 820,355 765,402 745,402"/>
    </g>
    <line x1="740" y1="406" x2="820" y2="406" stroke="var(--yellow)" stroke-width="1.5"/>
    <g fill="var(--yellow)">
      <polygon points="370,416 378,405 538,405 530,416"/>
    </g>
    <g fill="var(--white)">
      <rect x="380" y="405" width="3" height="11"/><rect x="392" y="405" width="3" height="11"/><rect x="404" y="405" width="3" height="11"/>
      <rect x="416" y="405" width="3" height="11"/><rect x="428" y="405" width="3" height="11"/><rect x="440" y="405" width="3" height="11"/>
      <rect x="452" y="405" width="3" height="11"/><rect x="464" y="405" width="3" height="11"/><rect x="476" y="405" width="3" height="11"/>
      <rect x="488" y="405" width="3" height="11"/><rect x="500" y="405" width="3" height="11"/><rect x="512" y="405" width="3" height="11"/>
    </g>
    <!-- lower photo -->
    <polygon points="592,667 820,667 820,818 500,818" fill="var(--black)"/>
    <polygon points="600,673 820,673 820,808 520,808" role="img" aria-label="Color photo of smiling gym members flexing in front of a confidence and esteem wall mural" fill="url(#photo2Grad)"/>
    <g fill="var(--black)">
      <polygon points="460,829 475,829 505,801 490,801"/>
      <polygon points="478,829 490,829 520,801 508,801"/>
    </g>
    <rect x="460" y="820" width="360" height="3" fill="var(--yellow)"/>
    <!-- tips section -->
    <polygon points="0,829 820,829 820,1045 456,1045 410,1127 0,1127" role="img" aria-label="Dark faded group photo of gym members" fill="url(#tipsGrad)"/>
  </svg>

  <div class="brand">
    <div class="brand-name">PeakForm</div>
    <div class="brand-tag">PERSONAL GROUP TRAINING</div>
  </div>

  <h1 class="title">Coral<br><span class="accent">Tide</span><br>Challenge</h1>

  <section class="card" style="left:39px;width:183px;height:320px">
    <div class="tab tab-protein" style="width:183px">Protein</div>
    <ul class="food-list protein">
      <li>4-6 oz Chicken Breast</li>
      <li>4-6oz Turkey Breast</li>
      <li>4-6 oz Filet Mignon</li>
      <li>4-6 oz Flank Steak</li>
      <li>4-6 oz Salmon</li>
      <li>4-6 oz Tuna</li>
      <li>4-6 oz Cod</li>
      <li>4-6 oz Cottage Cheese</li>
      <li>4-6 oz Greek Yogurt</li>
      <li>4-6 oz Tofu</li>
      <li>3 -5 egg whites +<br>1 whole egg</li>
    </ul>
  </section>

  <section class="card" style="left:239px;width:143px;height:320px">
    <div class="tab tab-fats" style="width:134px">Fats</div>
    <ul class="food-list fats">
      <li>¼ - ½ Avocado</li>
      <li>1 tbs Olive Oil</li>
      <li>1 small handful Almonds, Walnuts, Cashews</li>
    </ul>
  </section>

  <section class="card" style="left:400px;width:161px;height:320px">
    <div class="tab tab-carbs" style="width:161px">Carbs</div>
    <ul class="food-list carbs">
      <li>3 – 4oz Sweet Potato</li>
      <li>¼ - ½ cup White Rice</li>
      <li>¼ - ½ cup Quinoa</li>
      <li>¼ - ½ cup Oatmeal</li>
      <li>¾ cup Blueberries</li>
      <li>¾ cup Strawberries</li>
      <li>¾ cup Raspberries</li>
      <li>1 med. Apple</li>
      <li>1 small orange</li>
      <li>1 small grapefruit</li>
    </ul>
  </section>

  <section class="card" style="left:578px;width:205px;height:205px">
    <div class="tab tab-veg" style="width:202px">Vegetables</div>
    <ul class="food-list veg">
      <li>1 Scoop Powdered Greens</li>
      <li>1 Cup Sautéed Spinach</li>
      <li>1 Cup Sautéed Kale, Broccoli</li>
      <li>1 Cup Sautéed Bell Pepper</li>
      <li>1 Cup Sautéed Carrots</li>
      <li>1 Cup Sautéed Zucchini</li>
    </ul>
  </section>

  <div class="fuel-band"><span>Fuel Your Coral Tide!</span></div>

  <div class="tips">
    <div class="tip" style="left:70px;top:30px">
      <h3>Eat Like A Champion</h3>
      <p>Stick to this list as close as possible for maximum results, 7 Days A Week.</p>
    </div>
    <div class="tip" style="left:70px;top:114px">
      <h3>Burn More Than You Consume</h3>
      <p>This is the golden rule! You need to burn more calories than you consume to create a deficit and force your body to tap into fat stores for energy.</p>
    </div>
    <div class="tip" style="left:70px;top:208px">
      <h3>Prioritize Protein:</h3>
      <p>Protein helps build and maintain muscle mass, which is crucial for boosting metabolism and burning more calories at rest.</p>
    </div>
    <div class="tip" style="left:452px;top:30px;width:340px">
      <h3>Maximize Sleep</h3>
      <p>When sleep-deprived, your body produces more ghrelin (hunger hormone) and less leptin (satiety hormone). Aim for 7-8 hours of quality sleep nightly.</p>
    </div>
    <div class="tip" style="left:452px;top:124px;width:340px">
      <h3>Consistency Is King/Queen</h3>
      <p>Don't expect overnight results. Stick to your plan, track your progress, and celebrate small victories. Remember, slow and steady wins the shred race</p>
    </div>
  </div>

  <div class="visit"><span>Visit Us Our Website</span></div>
  <div class="url">www.joinpeakform.com</div>
</main>
</body>
</html>
```